Banner design

I need a banner designed that we will be putting on our gym walls. We need two banners but both will have the same design:
- One will be printed 12.2 X 2.5m
- One will be printed 9.4 X 2.5m
We are a kids gymnastics and cheerleading gym so are looking for something bright and fun that still looks professional.
Our colours are lime green, navy blue and white.
I have uploaded a couple of examples of what other gyms have done.
Kids

```html
<!DOCTYPE html>
<html lang="en">
<head>
<meta charset="utf-8">
<title>Brightleap Gymsports Wall Banner</title>
<link href="https://fonts.googleapis.com/css2?family=Roboto:wght@400;700&family=Exo+2:wght@800&display=swap" rel="stylesheet">
<style>
  :root {
    --page: #e9e9e9;
    --banner: #eeeff0;
    --navy: #14284b;
    --lime: #4fb833;
    --mint: #c4e0b8;
    --mist: #9aa5b4;
    --ink: #2a2f3a;
    --photo-teal: #3cc7b4;
    --photo-skin: #e4b79c;
    --garment-red: #b8343a;
    --garment-dark: #1b1b22;
  }
  html, body {
    margin: 0;
    padding: 0;
    width: 934px;
    height: 1200px;
    overflow: hidden;
    background: var(--page);
  }
  .canvas {
    position: relative;
    width: 934px;
    height: 1200px;
  }
  .banner {
    position: absolute;
    left: 53px;
    top: 490px;
    width: 828px;
    height: 220px;
    background: var(--banner);
    overflow: hidden;
    box-shadow: 3px 4px 8px rgba(0,0,0,0.35);
  }
  .banner__shapes {
    position: absolute;
    inset: 0;
  }
  .apparel-photos {
    position: absolute;
    left: 38px;
    top: 14px;
    width: 68px;
    height: 160px;
    border-radius: 4px;
    background: linear-gradient(180deg, var(--garment-red) 0%, var(--garment-red) 42%, var(--garment-dark) 58%, #1f2a55 100%);
  }
  .brand {
    margin: 0;
    color: var(--navy);
    font-family: "Exo 2", sans-serif;
    font-weight: 800;
  }
  .brand__name,
  .brand__sub {
    position: absolute;
    left: 190px;
    width: 300px;
    text-align: center;
    white-space: nowrap;
  }
  .brand__name {
    top: 28px;
    font-size: 50px;
    line-height: 70px;
  }
  .brand__sub {
    top: 112px;
    font-size: 23px;
    line-height: 26px;
    letter-spacing: 3px;
  }
  .blurb {
    position: absolute;
    left: 200px;
    top: 147px;
    width: 280px;
    margin: 0;
    font-family: "Roboto", sans-serif;
    font-size: 7.6px;
    line-height: 9.6px;
    text-align: center;
    color: var(--ink);
  }
  .follow {
    position: absolute;
    left: 290px;
    top: 184px;
    width: 100px;
    text-align: center;
    font-family: "Roboto", sans-serif;
    font-size: 7.6px;
    line-height: 10px;
    color: var(--navy);
  }
  .follow__links {
    display: flex;
    justify-content: center;
    gap: 8px;
    margin-top: 4px;
  }
  .follow__link {
    width: 12px;
    height: 12px;
    border-radius: 2px;
    background: var(--navy);
  }
  .follow__link--mid { background: #2b8fd6; }
  .follow__link--end { background: #d9533a; }
  .athlete-photo {
    position: absolute;
    left: 562px;
    top: 18px;
    width: 178px;
    height: 178px;
    border-radius: 50%;
    background: radial-gradient(circle at 50% 45%, var(--photo-teal) 0%, var(--photo-skin) 45%, #f6f6f6 75%);
  }
</style>
</head>
<body>
<main class="canvas">
  <section class="banner" aria-label="Brightleap Gymsports wall banner">
    <svg class="banner__shapes" width="828" height="220" viewBox="0 0 828 220" aria-hidden="true">
      <defs>
        <linearGradient id="navy-band" x1="0" x2="1" y1="0" y2="0">
          <stop offset="0" stop-color="#14284b" stop-opacity="0.85"/>
          <stop offset="0.6" stop-color="#14284b" stop-opacity="0.35"/>
          <stop offset="1" stop-color="#14284b" stop-opacity="0"/>
        </linearGradient>
      </defs>
      <polygon points="0,0 44,0 6,120 0,120" fill="#9aa5b4" opacity="0.8"/>
      <rect x="0" y="180" width="420" height="40" fill="url(#navy-band)"/>
      <polygon points="740,0 828,0 828,220 700,220 760,120" fill="#c4e0b8"/>
      <circle cx="651" cy="107" r="110" fill="none" stroke="#14284b" stroke-width="16"/>
      <circle cx="655" cy="110" r="124" fill="none" stroke="#14284b" stroke-width="3"/>
      <path d="M740 40 A118 118 0 0 1 735 190" fill="none" stroke="#14284b" stroke-width="5"/>
    </svg>
    <div class="apparel-photos" role="img" aria-label="Product photos of gym apparel: red top and crop, black tank, navy shorts set"></div>
    <h1 class="brand">
      <span class="brand__name">Brightleap</span>
      <span class="brand__sub">GYMSPORTS</span>
    </h1>
    <p class="blurb">Neque porro quisquam est qui dolorem ipsum quia dolor sit amet, consectetur, adipisci velitNeque porro quisquam est qui dolorem ipsum quia dolor sit amet, consectetur, adipisci velit</p>
    <div class="follow">
      FOLLOW US
      <div class="follow__links">
        <span class="follow__link"></span>
        <span class="follow__link follow__link--mid"></span>
        <span class="follow__link follow__link--end"></span>
      </div>
    </div>
    <div class="athlete-photo" role="img" aria-label="Photo of a young gymnast in a teal leotard doing a backbend"></div>
  </section>
</main>
</body>
</html>
```